Bright Lantern Studios Business Card Design

Doug Farley

Managing Partner

Doug@BrightLanternStudios.com

BrightLanternStudios.com

502-417-2356

Industry/Entity Type

Photographer

Contact Information for Business Card

Doug Farley

Managing Partner

Doug@BrightLanternStudios.com

BrightLanternStudios.com

502-417-2356

Requirements
Must have
• Must show that I am a pavlo trusted photographer

```html
<!DOCTYPE html>
<html lang="en">
<head>
<meta charset="utf-8">
<title>Bright Lantern Studios – Business Card</title>
<link rel="stylesheet" href="https://fonts.googleapis.com/css2?family=Josefin+Sans:wght@600&family=Montserrat:wght@400;600&display=swap">
<style>
  :root {
    --backdrop: #ecebe8;
    --card: #ffffff;
    --ink: #111111;
    --muted: #2a2a2a;
    --card-shadow: rgba(0, 0, 0, 0.14);
    --badge-fill: #e2e2e2;
  }
  * { margin: 0; padding: 0; box-sizing: border-box; }
  html, body {
    width: 1200px;
    height: 800px;
    overflow: hidden;
    background: var(--backdrop);
  }
  .canvas {
    position: relative;
    width: 1200px;
    height: 800px;
  }
  .card {
    position: absolute;
    top: 245px;
    width: 540px;
    height: 309px;
    background: var(--card);
    border-radius: 4px;
    box-shadow: 0 10px 28px var(--card-shadow);
    overflow: hidden;
    color: var(--ink);
  }
  .card--front { left: 45px; }
  .card--back { left: 615px; }

  /* Front */
  .front-brand {
    position: absolute;
    inset: 0;
    display: flex;
    flex-direction: column;
    align-items: center;
    justify-content: center;
    gap: 22px;
    padding: 0 24px;
  }
  .brand-dot {
    width: 54px;
    height: 54px;
    border-radius: 50%;
    background: var(--ink);
    flex: none;
  }
  .brand-name {
    font-family: "Josefin Sans", sans-serif;
    font-weight: 600;
    font-size: 32px;
    letter-spacing: 1px;
    text-transform: uppercase;
    color: var(--ink);
    white-space: nowrap;
  }

  /* Back */
  .holder {
    position: absolute;
    left: 40px;
    top: 40px;
    font-family: "Montserrat", sans-serif;
  }
  .holder-name {
    font-weight: 600;
    font-size: 18px;
    letter-spacing: 1.2px;
    text-transform: uppercase;
  }
  .holder-title {
    font-weight: 400;
    font-size: 14px;
    color: var(--muted);
    margin-top: 2px;
  }
  .contact-list {
    position: absolute;
    left: 40px;
    bottom: 42px;
    list-style: none;
    font-family: "Montserrat", sans-serif;
    font-size: 14px;
    color: var(--muted);
    display: flex;
    flex-direction: column;
    gap: 8px;
  }
  .contact-item {
    display: flex;
    align-items: center;
    gap: 10px;
  }
  .contact-icon {
    width: 13px;
    height: 13px;
    flex: none;
  }
  .back-brand {
    position: absolute;
    right: 34px;
    top: 88px;
    width: 190px;
    display: flex;
    flex-direction: column;
    align-items: center;
    gap: 14px;
  }
  .back-brand .brand-dot {
    width: 72px;
    height: 72px;
  }
  .back-brand .brand-name {
    font-size: 19px;
    text-align: center;
    line-height: 1.2;
    white-space: normal;
  }
  .trust-badge {
    position: absolute;
    right: 84px;
    bottom: 28px;
    width: 92px;
    height: 28px;
    border-radius: 14px;
    background: var(--badge-fill);
  }
</style>
</head>
<body>
<main class="canvas">

  <section class="card card--front" aria-label="Business card front">
    <div class="front-brand">
      <span class="brand-dot" aria-hidden="true"></span>
      <span class="brand-name">Bright Lantern Studios</span>
    </div>
  </section>

  <section class="card card--back" aria-label="Business card back">
    <div class="holder">
      <p class="holder-name">Doug Farley</p>
      <p class="holder-title">Managing Partner</p>
    </div>

    <ul class="contact-list">
      <li class="contact-item">
        <svg class="contact-icon" viewBox="0 0 24 24" aria-hidden="true"><path fill="#111" d="M6.6 10.8a15.1 15.1 0 0 0 6.6 6.6l2.2-2.2c.3-.3.7-.4 1-.2 1.1.4 2.3.6 3.6.6.6 0 1 .4 1 1V20c0 .6-.4 1-1 1A17 17 0 0 1 3 4c0-.6.4-1 1-1h3.5c.6 0 1 .4 1 1 0 1.3.2 2.5.6 3.6.1.3 0 .7-.2 1z"/></svg>
        <span>502-417-2356</span>
      </li>
      <li class="contact-item">
        <svg class="contact-icon" viewBox="0 0 24 24" aria-hidden="true"><path fill="#111" d="M2 5h20v14H2z"/><path fill="none" stroke="#fff" stroke-width="1.8" d="M2.5 5.5 12 13l9.5-7.5"/></svg>
        <span>Doug@BrightLanternStudios.com</span>
      </li>
      <li class="contact-item">
        <svg class="contact-icon" viewBox="0 0 24 24" aria-hidden="true"><g fill="none" stroke="#111" stroke-width="2"><circle cx="12" cy="12" r="10"/><ellipse cx="12" cy="12" rx="4.5" ry="10"/><path d="M2 12h20M4 7h16M4 17h16"/></g></svg>
        <span>BrightLanternStudios.com</span>
      </li>
    </ul>

    <div class="back-brand">
      <span class="brand-dot" aria-hidden="true"></span>
      <span class="brand-name">Bright Lantern Studios</span>
    </div>

    <div class="trust-badge" role="img" aria-label="Trusted photographer certification badge"></div>
  </section>

</main>
</body>
</html>
```